Home care agency

Current website QTRBLOOMS.com. Need to update and reformat to different pages. use my info from my current website

Target Market(s)

adult children

Industry/Entity Type

Home Health

Coding

Coded - Design and coding required

Number of Pages Required

4 page

Font styles to use
Sans Serif

Colors
3276b5
33a6d7
3277b5
85cae6
85acd3

```html
<!DOCTYPE html>
<html lang="en">
<head>
<meta charset="utf-8">
<title>Quarter Blooms Home Health Services – About Us</title>
<link href="https://fonts.googleapis.com/css2?family=Arimo:wght@400;700&display=swap" rel="stylesheet">
<style>
:root{
  --blue-dark:#3276b5;
  --blue-footer:#3277b5;
  --blue-bright:#33a6d7;
  --blue-light:#85cae6;
  --blue-soft:#85acd3;
  --stage:#9b9a98;
  --ink:#222;
  --muted:#777;
  --panel:#f5f6f5;
  --field:#f5f4f2;
}
*{box-sizing:border-box;margin:0;padding:0}
html,body{width:1078px;height:1200px;overflow:hidden;background:var(--stage);font-family:"Arimo",Helvetica,Arial,sans-serif}
.page{position:absolute;left:332px;top:157px;width:732px;height:1235px;background:#fff;transform:scale(0.5923);transform-origin:0 0;overflow:hidden}
.abs{position:absolute}

.topbar{left:0;top:0;width:732px;height:35px;background:var(--blue-bright);color:#fff;font-size:11px}
.topbar .item{position:absolute;top:10px;display:flex;align-items:center;gap:6px;white-space:nowrap}
.topbar .sep{opacity:.8;margin-left:4px}
.social{position:absolute;top:10px;display:flex;gap:8px;left:625px}
.social span{width:15px;height:15px;border:1.4px solid #fff;border-radius:50%}

.header{left:0;top:35px;width:732px;height:58px}
.brand{position:absolute;left:95px;top:18px;display:flex;align-items:center;gap:6px;font-size:11px;color:var(--blue-dark)}
.brand .dot{width:20px;height:20px;border:1.5px solid var(--blue-bright);border-radius:50%}
.nav a{position:absolute;top:24px;font-size:9px;font-weight:700;color:var(--ink);text-decoration:none}
.btn-inquiry{position:absolute;left:592px;top:16px;width:134px;height:28px;border-radius:14px;background:var(--blue-dark);color:#fff;font-size:11px;font-weight:700;display:flex;align-items:center;justify-content:center}

.titlebar{left:0;top:93px;width:732px;height:60px;background:var(--panel)}
.titlebar h1{position:absolute;left:15px;top:16px;font-size:22px;font-weight:400;color:var(--ink)}

.section-title{font-size:22px;font-weight:400;color:var(--ink)}
.portrait{left:22px;top:215px;width:227px;height:185px;background:linear-gradient(135deg,#cfd6dc 0%,#e9e6e2 40%,#5a3b3e 70%,#8b8fa8 100%)}
.caption{left:14px;top:414px;width:240px;text-align:center;color:var(--muted);font-size:13px;line-height:17px}
.caption strong{display:block;margin-bottom:3px}
.bio{left:260px;top:212px;width:455px;font-size:13.5px;line-height:16.4px;color:var(--muted);text-align:justify}
.bio p+p{margin-top:16px}
.bio a{color:var(--blue-dark);text-decoration:none}

.banner{left:0;top:496px;width:733px;height:186px;background:linear-gradient(100deg,#4d5f79 0%,#8c8a92 35%,#b2a9a4 60%,#7d8594 85%,#5d7a6a 100%)}
.banner h2{position:absolute;left:25px;top:34px;font-size:27px;line-height:33px;font-weight:700;color:#fff}
.btn-contact{position:absolute;left:562px;top:78px;width:153px;height:43px;border-radius:10px;background:var(--blue-light);color:#fff;font-size:13.5px;font-weight:700;display:flex;align-items:center;justify-content:center}

.advice{left:17px;top:697px}
.advice p{font-size:13px;color:var(--muted);margin-top:6px}
.field{position:absolute;background:var(--field);border:1.5px solid #aaa;color:#888;font-size:13.5px;padding:9px 16px}
.btn-send{left:21px;top:973px;width:122px;height:39px;background:var(--blue-dark);border:1.5px solid var(--blue-soft);color:#fff;font-size:13px;font-weight:700;display:flex;align-items:center;justify-content:center}
.advisor{left:462px;top:735px;width:244px;height:241px;background:linear-gradient(90deg,#fff 0%,#e8ecf2 40%,#243552 60%,#1c2a44 100%)}

.footer{left:0;top:1070px;width:732px;height:138px;background:var(--blue-footer);color:#fff}
.footer h3{position:absolute;font-size:12px;font-weight:700;display:flex;align-items:center;gap:4px;white-space:nowrap}
.footer h3::after{content:"";width:40px;height:1px;background:#fff}
.footer .small{position:absolute;font-size:8px;line-height:11px}
.contact-row{position:absolute;left:293px;display:flex;gap:10px;font-size:8px;line-height:9.5px}
.contact-row svg{flex:none}
.btn-download{position:absolute;left:471px;top:84px;width:174px;height:46px;border:2px solid #fff;border-radius:10px;text-align:center;font-weight:700;padding-top:9px}
.btn-download small{display:block;font-size:8.5px}
.btn-download span{font-size:12.5px}
.copyright{left:0;top:1208px;width:732px;height:27px;background:var(--blue-bright);color:#fff;font-size:8px;text-align:center;line-height:27px}
</style>
</head>
<body>
<div class="page">

  <div class="abs topbar">
    <div class="item" style="left:86px">
      <svg width="11" height="13" viewBox="0 0 12 14"><path d="M6 0a5 5 0 0 1 5 5c0 4-5 9-5 9S1 9 1 5a5 5 0 0 1 5-5z" fill="#fff"/><circle cx="6" cy="5" r="2" fill="#33a6d7"/></svg>
      PO Box 48, Bayview, MA 02099 <span class="sep">|</span>
    </div>
    <div class="item" style="left:258px">
      <svg width="14" height="14" viewBox="0 0 14 14"><circle cx="7" cy="7" r="6" fill="none" stroke="#fff" stroke-width="1.6"/><path d="M7 3.5V7H4.5" stroke="#fff" stroke-width="1.5" fill="none"/></svg>
      Mon - Fri 9:00am-5:00pm <span class="sep">|</span>
    </div>
    <div class="item" style="left:427px">
      <svg width="12" height="12" viewBox="0 0 12 12"><path d="M2 .5l2.3 2.3-1.2 1.6a7 7 0 0 0 4.5 4.5l1.6-1.2 2.3 2.3-1.5 1.5C5 11 1 7 .5 2z" fill="#fff"/></svg>
      555-014-2276.
    </div>
    <div class="social"><span></span><span></span><span></span></div>
  </div>

  <div class="abs header">
    <div class="brand"><span class="dot"></span>Quarter Blooms</div>
    <nav class="nav">
      <a style="left:368px">HOME</a>
      <a style="left:414px">ABOUT</a>
      <a style="left:461px">SERVICES</a>
      <a style="left:531px">CONTACT</a>
    </nav>
    <div class="btn-inquiry">CARE INQUIRY FORM</div>
  </div>

  <div class="abs titlebar"><h1>About Us</h1></div>

  <h2 class="abs section-title" style="left:27px;top:172px">Chairman Message</h2>
  <div class="abs portrait" role="img" aria-label="Portrait of the chairman, a nurse in a white coat seated in an armchair"></div>
  <div class="abs caption">
    <strong>Marianne Keller</strong>
    Chairman<br>Quarter Blooms Home Health Services
  </div>
  <div class="abs bio">
    <p>Quarter Blooms Home Health Services is owned and operated by Marianne Keller. Marianne is a registered nurse and has been in the health care system since 2001. She has specialized in home care, cardiology, trauma and critical care. She invests in future caregivers and has taught for the nursing programs at <a>Eastbrook University</a>, <a>Harbor Health Institute</a>, and <a>Linwood College</a>.</p>
    <p>All Quarter Blooms caregivers have extensive background checks and training regarding HIPAA compliance. We individualize the care of our clients in order to provide the best care possible in their home. Quarter Blooms also ensures full access and understanding of client care at all times with a caregiver binder in the client’s home at all times. This binder includes information on the client’s care plan along and the notes from their caregivers. This will allow all caregivers and the client’s family to have an understanding of the care being provided.</p>
  </div>

  <div class="abs banner" role="img" aria-label="Background photo of a caregiver comforting an elderly woman">
    <h2>The support of<br>Quarter Blooms Home Health Services<br>coordinator is always available</h2>
    <div class="btn-contact">CONTACT WITH US</div>
  </div>

  <div class="abs advice">
    <h2 class="section-title">Need an advice?</h2>
    <p>Please fill the fillowing fomr and send it to us</p>
  </div>
  <div class="field" style="left:22px;top:774px;width:190px;height:39px">Your Name</div>
  <div class="field" style="left:226px;top:774px;width:204px;height:39px;padding-left:10px">Your E-mail</div>
  <div class="field" style="left:22px;top:826px;width:408px;height:138px;padding-top:14px">Your Message</div>
  <div class="abs btn-send">SEND MESSAGE</div>
  <div class="abs advisor" role="img" aria-label="Photo of a smiling advisor in a navy business suit gesturing toward the form"></div>

  <div class="abs footer">
    <h3 style="left:110px;top:27px">CONTACT US</h3>
    <p class="small" style="left:110px;top:49px;width:162px">Thank you for considering Quarter Blooms Home for your care needs. Information about your medical conditions, care, and financial situation that you provide to us in writing, via email, on the phone (including information left on voice mails) is held in strictest confidence.</p>

    <h3 style="left:293px;top:27px">GET IN TOUCH</h3>
    <div class="contact-row" style="top:51px">
      <svg width="10" height="13" viewBox="0 0 12 14"><path d="M6 0a5 5 0 0 1 5 5c0 4-5 9-5 9S1 9 1 5a5 5 0 0 1 5-5z" fill="#fff"/><circle cx="6" cy="5" r="2" fill="#3277b5"/></svg>
      <span>Quarter Blooms Home Health Services<br>PO Box 48<br>Bayview, MA 02099</span>
    </div>
    <div class="contact-row" style="top:90px">
      <svg width="11" height="11" viewBox="0 0 12 12"><path d="M2 .5l2.3 2.3-1.2 1.6a7 7 0 0 0 4.5 4.5l1.6-1.2 2.3 2.3-1.5 1.5C5 11 1 7 .5 2z" fill="#fff"/></svg>
      <span>555-014-2276. (Office)</span>
    </div>
    <div class="contact-row" style="top:113px">
      <svg width="12" height="9" viewBox="0 0 12 9"><rect width="12" height="9" fill="#fff"/><path d="M0 0l6 5 6-5" stroke="#3277b5" fill="none"/></svg>
      <span>info@qtrblooms.com</span>
    </div>

    <h3 style="left:472px;top:24px">CONTACT ONLINE</h3>
    <p class="small" style="left:473px;top:45px;width:160px">To contact us online, please fill out the care inquiry form above and you will be contacted within 24-48 hours.</p>
    <div class="btn-download"><small>Download</small><span>Employment Application</span></div>
  </div>
  <div class="abs copyright">Quarter Blooms Home Health Services © 2019 All Right Reserved</div>

</div>
</body>
</html>
```